Brindle 48 Focus Wheel

We need a professional **framework wheel diagram** designed for our detection dog training manual.

Our business is **Brindle 48 Dog Training**, and this graphic represents our **Detection Training Model**.

Please use the **attached reference images** as a guide for the structure and layout of the wheel.

### What we need

1. **Full wheel graphic**

* Clean circular framework wheel
* Similar structure to the attached example
* Clear sections and text
* Professional training manual style
* Transparent background

2. **Individual segment pieces**

We also need the **inner sections broken into separate pieces** (like the second reference image).

This will allow us to place each section on different pages of the manual when explaining the concepts.

Each piece should look like a **slice of the wheel**.

### Style

The design should look:

• Professional
• Clean and modern
• Structured and easy to read
• Suitable for a training manual

Avoid cartoon styles or clipart.

### Colours

Please use our brand colour palette (see attached image):

* Dark navy blue
* Steel blue
* Light blue
* White
* Light grey
* Dark grey

### Files required

Final files must include:

* Vector files (AI or EPS)
* Transparent PNG
* High-resolution PDF

Please also provide **each segment exported individually**

```html
<!DOCTYPE html>
<html lang="en">
<head>
<meta charset="utf-8">
<title>Brindle 48 Focus Wheel – Detection Training Model</title>
<link rel="stylesheet" href="https://fonts.googleapis.com/css2?family=Poppins:wght@600&display=swap">
<style>
  :root {
    --navy-dark: #1f2a3b;
    --steel-blue: #314c69;
    --light-blue: #67a4bc;
    --white: #ffffff;
    --light-grey: #f4f4f4;
    --dark-grey: #5c5c5c;
    --divider-dark: #1f2a3b;
  }
  html, body {
    margin: 0;
    padding: 0;
    width: 1200px;
    height: 1200px;
    overflow: hidden;
    background: var(--white);
  }
  .canvas {
    width: 1200px;
    height: 1200px;
    display: block;
  }
  .wheel-text {
    font-family: "Poppins", sans-serif;
    font-weight: 600;
  }
  .ring-label {
    fill: var(--white);
    font-size: 33px;
    letter-spacing: 2px;
  }
  .hub-title {
    fill: #111111;
    font-size: 28px;
    letter-spacing: 2px;
  }
  .hub-brand {
    fill: var(--dark-grey);
    font-size: 17px;
  }
  .ring-divider { stroke: var(--white); stroke-width: 1; }
  .slice-divider { stroke: var(--divider-dark); stroke-width: 1; }
</style>
</head>
<body>
<svg class="canvas" viewBox="0 0 1200 1200" xmlns="http://www.w3.org/2000/svg" aria-label="Detection Training Model wheel">
  <defs>
    <path id="label-reinforcement" d="M600,195 A405,405 0 0 1 886.4,313.6"/>
    <path id="label-development" d="M288.9,911.1 A440,440 0 0 0 600,1040"/>
    <path id="hub-title-path" d="M570.2,681.8 A87,87 0 1 1 629.8,681.8"/>
  </defs>

  <!-- outer frame -->
  <circle class="outer-frame" cx="600" cy="600" r="540" fill="var(--navy-dark)"/>

  <!-- pillar ring -->
  <circle class="pillar-ring" cx="600" cy="600" r="480" fill="var(--steel-blue)"/>
  <g class="pillar-dividers">
    <line class="ring-divider" x1="600" y1="120" x2="600" y2="240"/>
    <line class="ring-divider" x1="600" y1="960" x2="600" y2="1080"/>
    <line class="ring-divider" x1="120" y1="600" x2="240" y2="600"/>
    <line class="ring-divider" x1="960" y1="600" x2="1080" y2="600"/>
    <line class="ring-divider" x1="260.6" y1="260.6" x2="345.4" y2="345.4"/>
    <line class="ring-divider" x1="939.4" y1="260.6" x2="854.6" y2="345.4"/>
    <line class="ring-divider" x1="260.6" y1="939.4" x2="345.4" y2="854.6"/>
    <line class="ring-divider" x1="939.4" y1="939.4" x2="854.6" y2="854.6"/>
  </g>
  <text class="wheel-text ring-label"><textPath href="#label-reinforcement" startOffset="50%" text-anchor="middle">Reinforcement</textPath></text>
  <text class="wheel-text ring-label"><textPath href="#label-development" startOffset="50%" text-anchor="middle">Development</textPath></text>

  <!-- accent ring -->
  <circle class="accent-ring" cx="600" cy="600" r="360" fill="var(--light-blue)"/>

  <!-- inner slices -->
  <circle class="slices-upper" cx="600" cy="600" r="300" fill="var(--white)"/>
  <path class="slices-lower" d="M300,600 A300,300 0 0 0 900,600 Z" fill="var(--light-grey)"/>
  <g class="slice-dividers">
    <line class="slice-divider" x1="714" y1="600" x2="900" y2="600"/>
    <line class="slice-divider" x1="486" y1="600" x2="300" y2="600"/>
    <line class="slice-divider" x1="692.2" y1="533" x2="842.7" y2="423.7"/>
    <line class="slice-divider" x1="635.2" y1="491.6" x2="692.7" y2="314.7"/>
    <line class="slice-divider" x1="564.8" y1="491.6" x2="507.3" y2="314.7"/>
    <line class="slice-divider" x1="507.8" y1="533" x2="357.3" y2="423.7"/>
    <line class="slice-divider" x1="680.6" y1="680.6" x2="812.1" y2="812.1"/>
    <line class="slice-divider" x1="600" y1="714" x2="600" y2="900"/>
    <line class="slice-divider" x1="519.4" y1="680.6" x2="387.9" y2="812.1"/>
  </g>

  <!-- hub -->
  <circle class="hub" cx="600" cy="600" r="114" fill="var(--white)" stroke="#333333" stroke-width="0.6"/>
  <text class="wheel-text hub-title"><textPath href="#hub-title-path" textLength="470" lengthAdjust="spacing">DETECTION TRAINING MODEL</textPath></text>
  <circle class="hub-brand-ring" cx="600" cy="600" r="50" fill="none" stroke="var(--dark-grey)" stroke-width="2"/>
  <text class="wheel-text hub-brand" x="600" y="606" text-anchor="middle">Brindle 48</text>
</svg>
</body>
</html>
```